Design a label for a new brand of Gin the UK called Velvet Whisker - featuring a cat

The gin is Velvet Whisker in Colour and owners of Velvet Whisker cats will be a target market - the bottle is very distinctive and lends itself to a square label.

The Marshmallow root used in the production will be a draw to customers. The bottle is flat with a large front face that lends itself to a striking design. There should be enough space around the label to show the blue gin in the bottle as this is a feature.

Target Market(s)

gin lovers who may also own a Velvet Whisker car - age group 30 - 60 primarily female

Font styles to use
Sans Serif
Script

Colors

Designer to choose colors to be used in the design.

Requirements
Must have
• The gin will be a Velvet Whisker colour so the label must standout or completment the gin in the bottle. Here is the bottle you are working with
• https://www.flaskhaven-supply.co.uk/Glass-bottles/700ml-clear-glass-bottle-Tevrin.html
• Must have 70cl and 40% abv
Nice to have
• The predominent botanical (other than juniper) is marshmallow root, this is quite a sweet gin. The reference to marshmallow root would be a nice to have.

```html
<!DOCTYPE html>
<html lang="en">
<head>
<meta charset="utf-8">
<title>Velvet Whisker Gin – Label</title>
<link rel="stylesheet" href="https://fonts.googleapis.com/css2?family=Cormorant+Garamond:ital,wght@0,600;1,500&family=Open+Sans:wght@400&display=swap">
<style>
  :root {
    --backdrop: #eef1f5;
    --label-white: #ffffff;
    --frame-gold: #c9a050;
    --frame-navy: #1c1b33;
    --label-pink: #ee8fbf;
    --ink: #1c1b33;
  }
  html, body {
    margin: 0;
    padding: 0;
    overflow: hidden;
  }
  body {
    width: 871px;
    height: 1200px;
    background: var(--backdrop);
  }
  .canvas {
    position: relative;
    width: 871px;
    height: 1200px;
    overflow: hidden;
  }
  .label-frame {
    position: absolute;
    left: 0;
    top: 0;
  }
  .cat-portrait {
    position: absolute;
    left: 315px;
    top: 298px;
    width: 242px;
    height: 230px;
    border-radius: 46% 46% 40% 40%;
    background: radial-gradient(ellipse at 50% 45%, #f4eef2 0%, #d9cdd6 45%, #3a3650 100%);
  }
  .brand-name {
    position: absolute;
    left: 66px;
    width: 739px;
    top: 588px;
    margin: 0;
    text-align: center;
    font-family: "Cormorant Garamond", serif;
    font-style: normal;
    font-weight: 600;
    font-size: 60px;
    letter-spacing: 3px;
    color: var(--ink);
    line-height: 1;
  }
  .spirit-type {
    position: absolute;
    left: 66px;
    width: 739px;
    top: 688px;
    margin: 0;
    text-align: center;
    font-family: "Cormorant Garamond", serif;
    font-style: italic;
    font-weight: 500;
    font-size: 46px;
    color: var(--ink);
    line-height: 1;
  }
  .spirit-type .dot {
    font-style: normal;
    font-size: 28px;
    vertical-align: middle;
    margin: 0 8px;
  }
  .bottle-spec {
    position: absolute;
    top: 843px;
    margin: 0;
    font-family: "Open Sans", sans-serif;
    font-size: 26px;
    color: var(--ink);
    line-height: 1;
  }
  .bottle-spec.volume { left: 86px; }
  .bottle-spec.strength { right: 86px; }
</style>
</head>
<body>
  <main class="canvas">
    <svg class="label-frame" width="871" height="1200" viewBox="0 0 871 1200" aria-hidden="true">
      <path class="frame-outer" d="M30,285 Q435.5,225 841,285 V955 H30 Z" fill="var(--label-white)"/>
      <path class="frame-gold" d="M42,295 Q435.5,237 829,295 V943 H42 Z" fill="var(--frame-gold)"/>
      <path class="frame-gap" d="M52,304 Q435.5,247 819,304 V933 H52 Z" fill="var(--label-white)"/>
      <path class="frame-navy" d="M56,308 Q435.5,251 815,308 V929 H56 Z" fill="var(--frame-navy)"/>
      <path class="label-field" d="M66,318 Q435.5,261 805,318 V919 H66 Z" fill="var(--label-pink)"/>
    </svg>

    <div class="cat-portrait" role="img" aria-label="Ink illustration of a grumpy Persian cat's face"></div>

    <h1 class="brand-name">VELVET WHISKER</h1>
    <p class="spirit-type"><span class="dot">•</span>GIN<span class="dot">•</span></p>

    <p class="bottle-spec volume">70cl</p>
    <p class="bottle-spec strength">40% abv</p>
  </main>
</body>
</html>
```